Technology Consulting
I need single sided standard sized Business Card [3.5" x 2"]
use something that looks conservative and contemporary
Simple
Mark Delaney
System's Engineer
48 Harrow Lane
mdelaney@quorvalenconsulting.com
http://www.quorvalenconsutling.com
use a font that looks conservative and contemporary

```html
<!DOCTYPE html>
<html lang="en">
<head>
<meta charset="utf-8">
<title>Quorvalen Consulting – Business Card</title>
<link href="https://fonts.googleapis.com/css2?family=Arimo:wght@400;700&display=swap" rel="stylesheet">
<style>
  :root {
    --backdrop: #e9e6e1;
    --card: #ffffff;
    --navy: #1d3f7a;
    --tab-blue: #2f64ad;
    --tab-dark: #173c75;
    --mark-grey: #4a4d52;
    --text: #3a3d42;
    --muted: #6b6f75;
    --rule: #b9bcc1;
  }
  * { box-sizing: border-box; margin: 0; padding: 0; }
  html, body {
    width: 1200px; height: 778px; overflow: hidden;
    background: var(--backdrop);
    font-family: "Arimo", Arial, sans-serif;
  }
  .canvas { position: relative; width: 1200px; height: 778px; }
  .card {
    position: absolute; left: 50px; top: 139px;
    width: 1100px; height: 500px;
    background: var(--card);
    border-radius: 40px;
    box-shadow: 0 6px 18px rgba(0,0,0,0.18);
  }
  .edge-tab {
    position: absolute; top: 54px; width: 26px; height: 393px;
    background: linear-gradient(90deg, var(--tab-dark), var(--tab-blue) 50%, var(--tab-dark));
  }
  .edge-tab--left { left: -6px; border-radius: 8px 14px 14px 8px; }
  .edge-tab--right { right: -6px; border-radius: 14px 8px 8px 14px; }

  .brand { position: absolute; left: 160px; top: 28px; display: flex; align-items: center; gap: 28px; }
  .brand-dot { width: 150px; height: 150px; border-radius: 50%; background: var(--mark-grey); }
  .brand-name { color: var(--navy); font-weight: 700; text-transform: uppercase; line-height: 1; }
  .brand-name .line-1 { display: block; font-size: 78px; letter-spacing: 4px; }
  .brand-name .line-2 { display: block; font-size: 44px; letter-spacing: 9px; margin-top: 6px; }

  .person { position: absolute; right: 578px; top: 290px; text-align: right; }
  .person-name { font-size: 33px; font-weight: 700; color: var(--navy); }
  .person-role { font-size: 26px; color: var(--muted); margin-top: 8px; }

  .divider { position: absolute; left: 543px; top: 272px; width: 2px; height: 130px; background: var(--rule); }

  .contact { position: absolute; left: 586px; top: 212px; list-style: none; font-size: 24px; color: var(--text); }
  .contact li { display: flex; align-items: center; height: 36px; }
  .contact li.address { margin-bottom: 12px; }
  .contact svg { width: 20px; height: 20px; margin-right: 8px; fill: var(--text); flex: none; }
</style>
</head>
<body>
<div class="canvas">
  <div class="card">
    <div class="edge-tab edge-tab--left"></div>
    <div class="edge-tab edge-tab--right"></div>

    <div class="brand">
      <div class="brand-dot"></div>
      <div class="brand-name">
        <span class="line-1">Quorvalen</span>
        <span class="line-2">Consulting.com</span>
      </div>
    </div>

    <div class="person">
      <p class="person-name">Mark Delaney</p>
      <p class="person-role">System's Engineer</p>
    </div>

    <div class="divider"></div>

    <ul class="contact">
      <li class="address">48 Harrow Lane</li>
      <li><svg viewBox="0 0 20 20"><path d="M5 2l3 4-2 2c1 2.5 3 4.5 6 6l2-2 4 3-2 3C9 17 3 11 2 4z"/></svg>555.014.2291</li>
      <li><svg viewBox="0 0 20 20"><path d="M6 1h8v18H6zM8 3v11h4V3z"/></svg>555.019.7730</li>
      <li><svg viewBox="0 0 20 20"><path d="M1 4h18v12H1zM3 6v.5l7 5 7-5V6l-7 5z"/></svg>mdelaney@quorvalenconsulting.com</li>
      <li><svg viewBox="0 0 20 20"><circle cx="10" cy="10" r="9"/><path d="M10 1v18M1 10h18M4 5h12M4 15h12" stroke="#fff" stroke-width="1.2" fill="none"/></svg>www.quorvalenconsulting.com</li>
    </ul>
  </div>
</div>
</body>
</html>
```